lifestyle photographer promotion piece

I would like to create a printed postcard to send to potential clients to introduce them to my work and hopefully create new clients. I'm a commercial photographer who just relocated to the Miami area and would really like to be getting more luxury lifestyle and resort work that includes my unique ability to shoot every aspect of lifestyle including food, travel, lifestyle and fashion. I'd like to incorporate between 4-12 of my best images from my online portfolio at www.lunadekkerfoto.com. The printed piece should also have a very clean, graphic, modern feel to it overall similar to my website. The main goal is to create a striking and compelling grouping of images showing my diverse offerings but in a way that shows an obvious visual style, my style. Please refer to my website for images. When winner is chosen, I will supply hi-res files to compete the design.
Updates

The card is a mailer and a handout. The back of the card should be black and white and text only with my info and an area for address to information. Dimensions of the card are 6x8.5 inches and I prefer the horizontal aspect ratio.

I've noticed a few designers are incorporating graphics. I would like to avoid that. Interested in photography dominated card with /or without graphic use of white space. I tend to avoid color backgrounds, white space is my preference in most cases although I'm not completely against it. 

Target Market(s)

Advertising Agencies and Magazines, Record Labels, Modeling Agencies, Public Relations Firms

Industry/Entity Type

Fashion

Requirements
Must have
• Horizontal

Front(color):
Marisol Tate Photography
Miami / Naples / New York

Back(black and white):
(239)614-2938
www.lunadekkerfoto.com
info@lunadekkerfoto.com

```html
<!DOCTYPE html>
<html lang="en">
<head>
<meta charset="utf-8">
<title>Marisol Tate Photography — Postcard Back</title>
<link rel="stylesheet" href="https://fonts.googleapis.com/css2?family=Oswald:wght@300&display=swap">
<style>
  :root {
    --ink: #1b1b1d;
    --paper: #ffffff;
  }
  html, body {
    margin: 0;
    padding: 0;
    width: 1200px;
    height: 846px;
    overflow: hidden;
    background: var(--paper);
  }
  .card-back {
    position: relative;
    width: 1200px;
    height: 846px;
    background: var(--paper);
  }
  .contact-band {
    position: absolute;
    left: 0;
    top: 0;
    width: 1200px;
    height: 513px;
    background: var(--ink);
  }
  .corner-mark {
    position: absolute;
    left: 25px;
    top: 27px;
  }
  .contact-list {
    position: absolute;
    left: 0;
    top: 164px;
    width: 1175px;
    margin: 0;
    padding: 0;
    list-style: none;
    text-align: center;
    font-family: "Oswald", "Bodoni Moda", serif;
    font-weight: 300;
    color: var(--paper);
    font-size: 48px;
    line-height: 72px;
    letter-spacing: 0.16em;
    transform: scaleX(0.9);
    transform-origin: center;
  }
  .contact-list .phone { letter-spacing: 0.12em; }
  .divider-rule {
    position: absolute;
    left: 121px;
    top: 415px;
    width: 925px;
    height: 6px;
    background: var(--paper);
  }
</style>
</head>
<body>
  <main class="card-back">
    <section class="contact-band">
      <svg class="corner-mark" width="122" height="106" viewBox="0 0 122 106" aria-hidden="true">
        <polygon points="0,0 122,0 0,106" fill="#ffffff"/>
      </svg>
      <ul class="contact-list">
        <li class="phone">(239)614-2938</li>
        <li class="website">www.lunadekkerfoto.com</li>
        <li class="email">info@lunadekkerfoto.com</li>
      </ul>
      <div class="divider-rule"></div>
    </section>
  </main>
</body>
</html>
```